Fiber to the Home Business - Coming Soon Postcard

Qorvane Communications is looking for a postcard design that we can mail out to potential customers in areas that we are building our Fiber Optic network. The wording on this postcard needs to include:
Fiber Internet, Phone, HD TV.
Coming soon to your area.
Contact us now to schedule.
(318) 406-2917
Qorvane.com/fiber
Back of postcard:
Mailing information area.
Keep your same phone number
Unlimited Nationwide Long Distance
All for $19.99/month
Internet Speeds up to 150Mbps
Starting at $39.99/month
High Definition TV
Packages starting at $50/month
No Contract Required.
Industry/Entity Type
Internet Service Provider
Requirements
Must have
- Catchy background graphics on front of postcard geared toward happy internet customers.
Should not have
- Cable

```html
<!DOCTYPE html>
<html lang="en">
<head>
<meta charset="utf-8">
<title>Qorvane Communications – Fiber Coming Soon Postcard</title>
<link href="https://fonts.googleapis.com/css2?family=Montserrat:wght@400;500;600;700&display=swap" rel="stylesheet">
<style>
  :root {
    --navy: #123f8a;
    --royal: #1c5cb0;
    --sky: #4db4ec;
    --sky-light: #8fd0f4;
    --orange: #f26b1d;
    --slate: #5c6670;
    --white: #ffffff;
    --paper: #f5f3f4;
    --stage: #e6e4e2;
  }
  * { box-sizing: border-box; margin: 0; padding: 0; }
  html, body { width: 1200px; height: 1000px; overflow: hidden; }
  body {
    background: var(--stage);
    font-family: "Montserrat", Arial, sans-serif;
    position: relative;
  }
  .postcard {
    position: absolute;
    background: var(--white);
    overflow: hidden;
  }
  .postcard-front { left: 34px; top: 25px; width: 599px; height: 464px; }
  .postcard-back { left: 565px; top: 507px; width: 600px; height: 465px; background: var(--paper); }
  .postcard svg.art { position: absolute; inset: 0; }

  /* front */
  .headline-badge {
    position: absolute; left: 38px; top: 150px; width: 180px; height: 180px;
    border-radius: 50%; background: var(--navy); border: 5px solid var(--royal);
    display: flex; flex-direction: column; justify-content: center; align-items: center;
    text-align: center; line-height: 1.18;
  }
  .headline-services { color: var(--white); font-weight: 600; font-size: 21px; }
  .headline-soon { color: var(--orange); font-weight: 600; font-size: 20px; margin-top: 4px; }
  .front-contact { position: absolute; left: 17px; top: 386px; color: var(--white); }
  .front-contact .lead { font-size: 12.5px; font-style: italic; font-weight: 400; margin-bottom: 6px; }
  .contact-line { display: flex; align-items: center; gap: 5px; font-size: 15px; font-weight: 500; margin-bottom: 5px; }
  .contact-line svg { width: 11px; height: 11px; }
  .brand-name {
    position: absolute; display: flex; align-items: center; gap: 8px;
    color: var(--slate); font-weight: 600; line-height: 1.05;
  }
  .brand-name .dot { width: 14px; height: 14px; border-radius: 50%; background: var(--sky); flex: none; }
  .front-brand { right: 24px; top: 372px; font-size: 27px; }
  .front-brand small, .back-brand small { display: block; font-size: 0.52em; letter-spacing: 2px; }

  /* back */
  .back-top { position: absolute; left: 0; top: 0; width: 450px; height: 150px; background: var(--white); }
  .back-brand { left: 30px; top: 82px; font-size: 27px; }
  .back-contact { position: absolute; left: 252px; top: 28px; color: #222; }
  .back-contact .contact-line:first-child { font-size: 19px; }
  .back-contact .contact-line { font-size: 12px; margin-bottom: 3px; }
  .no-contract {
    position: absolute; left: 268px; top: 88px; width: 160px; text-align: center;
    color: var(--orange); font-weight: 700; font-size: 19px; line-height: 1.12;
  }
  .offer-panel { position: absolute; left: 0; top: 150px; width: 290px; height: 231px; background: var(--navy); }
  .offer-strip { position: absolute; left: 0; top: 381px; width: 75px; height: 84px; background: var(--navy); }
  .offer { position: absolute; left: 28px; width: 250px; height: 58px; }
  .offer-icon {
    position: absolute; left: 0; top: 2px; width: 54px; height: 54px; border-radius: 50%;
    background: var(--white); display: flex; align-items: center; justify-content: center;
  }
  .offer-icon svg { width: 34px; height: 34px; }
  .offer-box {
    position: absolute; left: 50px; top: 0; width: 198px; height: 58px;
    background: var(--sky); border: 1.5px dashed var(--white); border-radius: 5px;
    text-align: center; display: flex; flex-direction: column; justify-content: center;
    color: #0d1f3a; font-size: 11.5px; font-weight: 500; line-height: 1.2;
  }
  .offer-box strong { color: var(--white); font-size: 13.5px; font-weight: 700; }
  .mailing-area { position: absolute; left: 75px; top: 381px; width: 525px; height: 84px; }
</style>
</head>
<body>

<section class="postcard postcard-front">
  <svg class="art" viewBox="0 0 599 464" width="599" height="464">
    <defs>
      <linearGradient id="photoTone" x1="0" y1="0" x2="1" y2="1">
        <stop offset="0" stop-color="#cfc8bd"/>
        <stop offset="0.5" stop-color="#a58a74"/>
        <stop offset="1" stop-color="#3d4f9a"/>
      </linearGradient>
    </defs>
    <path role="img" aria-label="Photo of a smiling girl resting her chin on her hand at a computer"
          d="M0 0 H599 V205 C470 250 360 300 230 315 C140 322 60 290 0 262 Z" fill="url(#photoTone)"/>
    <path d="M0 262 C60 290 140 322 230 315 C360 300 470 250 599 205 V225 C470 270 360 318 230 330 C140 336 60 308 0 285 Z" fill="var(--royal)"/>
    <path d="M0 285 C60 308 140 336 230 330 C360 318 470 270 599 225 V238 C470 285 360 335 240 345 C150 350 60 322 0 300 Z" fill="var(--sky)"/>
    <path d="M0 355 C120 345 250 350 330 378 C390 400 420 430 440 464 H0 Z" fill="var(--sky)"/>
    <path d="M0 362 C120 352 245 358 322 385 C380 406 408 434 425 464 H0 Z" fill="var(--navy)"/>
  </svg>

  <div class="headline-badge">
    <p class="headline-services">Fiber Internet,<br>Phone, HD TV.</p>
    <p class="headline-soon">Coming Soon<br>to your area.</p>
  </div>

  <div class="brand-name front-brand"><span class="dot"></span><span>Qorvane<small>COMMUNICATIONS</small></span></div>

  <div class="front-contact">
    <p class="lead">Contact us now to schedule</p>
    <p class="contact-line"><svg viewBox="0 0 12 12"><circle cx="6" cy="6" r="5.3" fill="none" stroke="#fff"/><path d="M4 3.2l1 1.4-.6.7c.4.9 1 1.5 1.9 1.9l.7-.6 1.4 1-.6 1c-2.3-.3-4.2-2.2-4.5-4.5z" fill="#fff"/></svg>(318) 406-2917</p>
    <p class="contact-line"><svg viewBox="0 0 12 12"><circle cx="6" cy="6" r="5.3" fill="none" stroke="#fff"/><path d="M.8 6h10.4M6 .8c-2.5 3-2.5 7.4 0 10.4M6 .8c2.5 3 2.5 7.4 0 10.4" fill="none" stroke="#fff" stroke-width=".8"/></svg>www.Qorvane.com/fiber</p>
  </div>
</section>

<section class="postcard postcard-back">
  <div class="back-top"></div>
  <div class="brand-name back-brand"><span class="dot"></span><span>Qorvane<small>COMMUNICATIONS</small></span></div>
  <div class="back-contact">
    <p class="contact-line"><svg viewBox="0 0 12 12"><circle cx="6" cy="6" r="5.3" fill="none" stroke="var(--royal)"/><path d="M4 3.2l1 1.4-.6.7c.4.9 1 1.5 1.9 1.9l.7-.6 1.4 1-.6 1c-2.3-.3-4.2-2.2-4.5-4.5z" fill="var(--royal)"/></svg>(318) 406-2917</p>
    <p class="contact-line"><svg viewBox="0 0 12 12"><circle cx="6" cy="6" r="5.3" fill="none" stroke="var(--royal)"/><path d="M.8 6h10.4M6 .8c-2.5 3-2.5 7.4 0 10.4M6 .8c2.5 3 2.5 7.4 0 10.4" fill="none" stroke="var(--royal)" stroke-width=".8"/></svg>www.Qorvane.com/fiber</p>
  </div>
  <p class="no-contract">NO CONTRACT<br>REQUIRED</p>

  <div class="offer-panel">
    <div class="offer" style="top:20px">
      <div class="offer-box">Unlimited Nationwide<br>Long Distance<strong>All for $19.99/month</strong></div>
      <div class="offer-icon"><svg viewBox="0 0 34 34"><path d="M4 12c8-6 18-6 26 0l-3 4-5-2v-3c-3-1-7-1-10 0v3l-5 2z" fill="var(--navy)"/><path d="M9 18h16l3 10H6z" fill="var(--navy)"/><circle cx="17" cy="23" r="3" fill="#fff"/></svg></div>
    </div>
    <div class="offer" style="top:90px">
      <div class="offer-box">Internet Speeds upto<br>150Mbps<strong>Starting at $39.99/mnth</strong></div>
      <div class="offer-icon"><svg viewBox="0 0 34 34"><path d="M4 24a13 13 0 0 1 26 0z" fill="var(--navy)"/><path d="M8 22a9 9 0 0 1 18 0" fill="none" stroke="#fff" stroke-width="1.5" stroke-dasharray="2 2"/><path d="M17 23l6-8" stroke="#fff" stroke-width="2.2" stroke-linecap="round"/><circle cx="17" cy="23" r="2" fill="#fff"/></svg></div>
    </div>
    <div class="offer" style="top:160px">
      <div class="offer-box">Hight Definition TV<strong>Packages starting at<br>$50/month</strong></div>
      <div class="offer-icon"><svg viewBox="0 0 34 34"><rect x="4" y="7" width="26" height="17" rx="1.5" fill="none" stroke="var(--navy)" stroke-width="2.5"/><text x="17" y="20" text-anchor="middle" font-family="Montserrat, Arial, sans-serif" font-size="9" font-weight="700" font-style="italic" fill="var(--navy)">HD</text><path d="M12 28h10M17 24v4" stroke="var(--navy)" stroke-width="2.5"/></svg></div>
    </div>
  </div>
  <div class="offer-strip"></div>
  <div class="mailing-area" aria-label="Mailing information area"></div>
</section>

</body>
</html>
```